Need Business Card for our Real Estate Business with Sales Executive's Picture

PANTONE 484 C ( RED)

PANTONE 2766 C ( BLUE

Industry/Entity Type

Real Estate

Contact Information for Business Card

Name, Mobile, email, & picture of Person
Agency Phone, address, Web address

Requirements
Must have
• Our Logo Colours, Agent Picture,

```html
<!DOCTYPE html>
<html lang="en">
<head>
<meta charset="utf-8">
<title>Meridian Real Estate – Business Card</title>
<link href="https://fonts.googleapis.com/css2?family=Cinzel:wght@500&family=Lato:wght@400&display=swap" rel="stylesheet">
<style>
  :root {
    --navy: #0b1640;
    --maroon: #7a1219;
    --ink: #1c2452;
    --paper: #ffffff;
    --stage: #e6e7ea;
    --photo-a: #e9e4de;
    --photo-b: #2a3f8f;
  }
  * { box-sizing: border-box; margin: 0; padding: 0; }
  html, body { width: 1200px; height: 900px; overflow: hidden; }
  body { background: var(--stage); position: relative; font-family: "Lato", sans-serif; }

  .card {
    position: absolute;
    width: 640px;
    height: 365px;
    overflow: hidden;
    box-shadow: 0 10px 28px rgba(0,0,0,.22);
  }

  /* Front */
  .card-front { left: 80px; top: 60px; background: var(--navy); }
  .card-front .sweep { position: absolute; inset: 0; }
  .brand {
    position: absolute;
    left: 300px;
    top: 140px;
    display: flex;
    align-items: center;
    gap: 14px;
  }
  .brand-square { width: 22px; height: 22px; background: var(--maroon); }
  .brand-name {
    font-family: "Cinzel", serif;
    font-weight: 500;
    font-size: 26px;
    letter-spacing: 2px;
    color: var(--paper);
  }

  /* Back */
  .card-back { left: 480px; top: 470px; background: var(--paper); }
  .agent-photo {
    position: absolute;
    left: 88px;
    top: 92px;
    width: 184px;
    height: 184px;
    border-radius: 50%;
    border: 2px solid var(--navy);
    padding: 6px;
    background: var(--paper);
  }
  .agent-photo div {
    width: 100%;
    height: 100%;
    border-radius: 50%;
    background: radial-gradient(circle at 50% 35%, var(--photo-a) 0 45%, var(--photo-b) 75%);
  }
  .divider {
    position: absolute;
    left: 318px;
    top: 58px;
    width: 2px;
    height: 250px;
    background: var(--maroon);
  }
  .details { position: absolute; left: 342px; top: 60px; color: var(--ink); }
  .agent-name {
    font-family: "Cinzel", serif;
    font-weight: 500;
    font-size: 27px;
    letter-spacing: 1px;
    color: var(--maroon);
    line-height: 1.1;
    margin-bottom: 6px;
  }
  .address { font-size: 17px; line-height: 1.3; margin-bottom: 8px; }
  .contact-list { list-style: none; font-size: 17px; line-height: 1.55; }
  .contact-list li { display: flex; align-items: center; gap: 10px; }
  .contact-list svg { width: 14px; height: 14px; fill: var(--maroon); flex: none; }
</style>
</head>
<body>

<section class="card card-front" aria-label="Card front">
  <svg class="sweep" viewBox="0 0 640 365" preserveAspectRatio="none" aria-hidden="true">
    <path d="M0 365 C 170 300, 420 230, 640 170 L 640 365 Z" fill="#ffffff"/>
    <path d="M0 365 C 170 320, 420 250, 640 200 L 640 365 Z" fill="#0b1640" opacity="0"/>
  </svg>
  <div class="brand">
    <span class="brand-square"></span>
    <span class="brand-name">Meridian Real Estate</span>
  </div>
</section>

<section class="card card-back" aria-label="Card back">
  <div class="agent-photo"><div role="img" aria-label="Portrait photo of the sales executive in a blue suit"></div></div>
  <span class="divider"></span>
  <div class="details">
    <h1 class="agent-name">Daniel Reyes</h1>
    <p class="address">2210 Lakeview Avenue Suite 400<br>Maple Grove, IL 60421</p>
    <ul class="contact-list">
      <li><svg viewBox="0 0 24 24"><path d="M6.6 10.8a15 15 0 0 0 6.6 6.6l2.2-2.2a1 1 0 0 1 1-.25 11.4 11.4 0 0 0 3.6.57 1 1 0 0 1 1 1V20a1 1 0 0 1-1 1A17 17 0 0 1 3 4a1 1 0 0 1 1-1h3.5a1 1 0 0 1 1 1c0 1.25.2 2.45.57 3.57a1 1 0 0 1-.25 1z"/></svg>(09) 555 0142</li>
      <li><svg viewBox="0 0 24 24"><path d="M7 1h10a2 2 0 0 1 2 2v18a2 2 0 0 1-2 2H7a2 2 0 0 1-2-2V3a2 2 0 0 1 2-2zm0 3v14h10V4zm5 15.5a1 1 0 1 0 0 2 1 1 0 0 0 0-2z"/></svg>027 555 0198</li>
      <li><svg viewBox="0 0 24 24"><path d="M2 5h20v14H2zm2 2v.5l8 5 8-5V7z"/></svg>daniel@meridianhomes.com</li>
      <li><svg viewBox="0 0 24 24"><path d="M12 2a10 10 0 1 0 0 20 10 10 0 0 0 0-20zm6.9 9h-3a15 15 0 0 0-1.3-5.6A8 8 0 0 1 18.9 11zM12 4.1c.9 1.3 1.7 3.7 1.9 6.9h-3.8c.2-3.2 1-5.6 1.9-6.9zM9.4 5.4A15 15 0 0 0 8.1 11h-3a8 8 0 0 1 4.3-5.6zM5.1 13h3a15 15 0 0 0 1.3 5.6A8 8 0 0 1 5.1 13zm6.9 6.9c-.9-1.3-1.7-3.7-1.9-6.9h3.8c-.2 3.2-1 5.6-1.9 6.9zm2.6-1.3a15 15 0 0 0 1.3-5.6h3a8 8 0 0 1-4.3 5.6z"/></svg>www.meridianhomes.com</li>
    </ul>
  </div>
</section>

</body>
</html>
```